Lanternfield Golf

I want main multi colored logo, with designer choosing a background of their choice for overall page, and then second upload (logo’s font) underneath, with address logo (but with following added right below phone number along with zip Code):

418 Calloway St
Suite 307C
Jersey City, NJ, 07348

a below a bit further down - to start.

Then we’ll take next steps.

```html
<!DOCTYPE html>
<html lang="en">
<head>
<meta charset="utf-8">
<title>Lanternfield Golf</title>
<link href="https://fonts.googleapis.com/css2?family=Poppins:wght@400;500;600;700&display=swap" rel="stylesheet">
<style>
:root{
  --navy:#2b3152;
  --navy-deep:#262c4b;
  --gold:#e4a812;
  --gold-bright:#f0b519;
  --btn:#fbd37f;
  --btn-edge:#e9b54f;
  --link:#2f5aa6;
  --text:#4a4f63;
  --muted:#b9bcc6;
  --soft:#f2f2f2;
  --white:#ffffff;
}
*{box-sizing:border-box;margin:0;padding:0}
html,body{width:1200px;height:4138px;overflow:hidden}
body{position:relative;background:var(--white);font-family:'Poppins',sans-serif;color:var(--text)}
.btn{position:absolute;display:flex;align-items:center;justify-content:center;background:var(--btn);color:var(--navy);font-weight:600;font-size:13px;border-radius:0 10px 0 10px;box-shadow:0 3px 0 var(--btn-edge)}
.section-title{position:absolute;left:0;width:1200px;text-align:center;font-weight:600;font-size:40px;color:var(--navy);letter-spacing:.5px}

/* header */
.site-header{position:absolute;left:0;top:0;width:1200px;height:148px;background:var(--white)}
.brand{position:absolute;left:150px;top:34px;display:flex;gap:12px;align-items:center}
.brand-mark{width:86px;height:86px;background:var(--navy);flex:none}
.brand-text{color:var(--navy);line-height:1.15}
.brand-owner{font-size:12px;font-weight:600}
.brand-name{font-size:12px;font-weight:600;text-transform:uppercase}
.brand-line{font-size:8.5px;font-weight:500}
.brand-phone{font-size:11px;font-weight:500}
.top-btn{position:absolute;top:39px;height:36px;display:flex;align-items:center;justify-content:center;gap:6px;color:#fff;font-size:13px;font-weight:600;border-radius:0 10px 0 10px}
.top-btn.phone{left:800px;width:159px;background:var(--gold)}
.top-btn.chat{left:968px;width:122px;background:var(--navy)}
.main-nav{position:absolute;top:102px;left:0;font-size:14px;font-weight:500;color:var(--navy)}
.main-nav span{position:absolute;white-space:nowrap}
.main-nav .active{color:var(--link)}

/* hero */
.hero{position:absolute;left:0;top:148px;width:1200px;height:565px;background:linear-gradient(135deg,#8f9868 0%,#6f8240 50%,#56702a 100%)}
.hero-title{position:absolute;left:624px;top:212px;width:400px;text-align:center;color:#fff;font-weight:600;font-size:50px;line-height:58px;letter-spacing:1px}
.hero .btn{left:764px;top:352px;width:121px;height:36px}

/* about */
.about-photo{position:absolute;left:93px;top:809px;width:447px;height:376px;background:linear-gradient(135deg,#8fb556 0%,#6b9838 100%);clip-path:polygon(0 0,405px 0,405px 52px,447px 52px,447px 376px,0 376px)}
.about-title{position:absolute;left:586px;top:832px;font-size:36px;font-weight:600;line-height:42px;color:var(--navy)}
.about-copy{position:absolute;left:586px;top:936px;width:470px;font-size:13.3px;line-height:20.6px}
.about .btn{left:588px;top:1132px;width:120px;height:36px}

/* courses */
.courses{position:absolute;left:0;top:1285px;width:1200px;height:663px;background:var(--soft)}
.course-card{position:absolute;top:1445px;width:277px;height:383px;background:#fff;border:2px solid #e6e4da;border-radius:0 12px 0 0}
.course-photo{width:100%;height:196px;border-radius:0 10px 0 0}
.course-name{margin:28px 20px 0;text-align:center;font-size:17px;font-weight:600;line-height:21px;color:var(--navy)}
.course-desc{margin:10px 36px 0;text-align:center;font-size:11.5px;line-height:16px}
.course-card .btn{left:79px;top:329px;width:119px;height:34px}
.slider-arrow{position:absolute;top:1538px}

/* discover */
.discover{position:absolute;left:0;top:1948px;width:1200px;height:579px;background:var(--navy)}
.discover-photo{position:absolute;left:0;top:0;width:1200px;height:579px;background:linear-gradient(160deg,#5a8fbb 0%,#9aaec0 50%,#a8987c 100%);clip-path:polygon(612px 0,1200px 0,1200px 579px,612px 579px,522px 300px)}
.discover-accent{position:absolute;left:0;top:0;width:1200px;height:579px;background:var(--gold-bright);clip-path:polygon(600px 60px,612px 60px,532px 300px,612px 540px,600px 540px,508px 300px)}
.discover-title{position:absolute;left:150px;top:118px;font-size:40px;line-height:40px;font-weight:700;color:#fff}
.discover-copy{position:absolute;left:150px;top:232px;width:305px;font-size:14px;line-height:20.5px;color:#fff}
.discover .btn{left:150px;top:370px;width:120px;height:36px}

/* team */
.member{position:absolute;top:2715px;width:263px;text-align:center}
.member-photo{width:263px;height:263px;border-radius:50%}
.member-name{margin-top:12px;font-size:20px;font-weight:500;color:var(--gold)}
.member-role{font-size:14px;font-weight:500;color:var(--link);margin-top:-2px}

/* events */
.events{position:absolute;left:0;top:3124px;width:1200px;height:602px;background:linear-gradient(135deg,#66723f 0%,#7b8646 50%,#5f6d31 100%)}
.events .section-title{top:48px;color:#fff;z-index:1}
.event-list{position:absolute;left:138px;top:123px;width:280px;height:413px;background:var(--gold-bright);color:#fff}
.event{position:absolute;left:30px}
.event-date{display:flex;align-items:center;gap:4px;font-size:11px;font-weight:600}
.event-title{font-size:15.5px;font-weight:600;line-height:20px;margin-top:8px;width:235px}
.calendar{position:absolute;left:462px;top:123px;width:592px;height:413px;background:#fff}
.cal-month{position:absolute;left:40px;top:22px;font-size:20px;color:var(--navy)}
.cal-next{position:absolute;left:182px;top:29px}
.cal-add{position:absolute;left:498px;top:30px;display:flex;align-items:center;gap:4px;font-size:8px;color:#4aa85a}
.cal-grid{position:absolute;left:12px;top:98px;font-size:13px;color:var(--navy)}
.cal-grid span{position:absolute;width:60px;margin-left:-30px;text-align:center}
.cal-grid .head{font-size:10px;font-weight:600}
.cal-grid .off{color:#e3e3e6}
.cal-grid .dim{color:var(--muted)}
.dot{position:absolute;width:4px;height:4px;border-radius:50%}

/* footer */
.site-footer{position:absolute;left:0;top:3726px;width:1200px;height:412px;background:#fff}
.footer-brand{position:absolute;left:150px;top:124px;display:flex;gap:10px;align-items:center}
.divider{position:absolute;top:0;width:1px;height:318px;background:#dcdce2}
.footer-col-title{position:absolute;top:66px;font-size:19px;font-weight:600;color:var(--navy)}
.footer-links{position:absolute;left:424px;top:107px;font-size:13.5px;line-height:26.4px;color:var(--navy)}
.contact-item{position:absolute;left:569px;display:flex;gap:10px;font-size:13.5px;line-height:17px;color:var(--navy)}
.contact-icon{width:34px;height:34px;border-radius:50%;background:var(--gold);display:flex;align-items:center;justify-content:center;flex:none}
.news-copy{position:absolute;left:825px;top:110px;width:240px;font-size:13.5px;line-height:21px;color:var(--navy)}
.news-input{position:absolute;left:830px;top:162px;width:238px;height:44px;border-radius:22px;background:#eeeeee;padding-left:20px;display:flex;align-items:center;font-size:13px;color:var(--navy)}
.news-btn{position:absolute;left:832px;top:223px;width:124px;height:37px;border-radius:19px;background:var(--gold);color:#fff;font-weight:600;font-size:13px;display:flex;align-items:center;justify-content:center}
.footer-rule{position:absolute;left:138px;top:318px;width:922px;height:1px;background:#dcdce2}
.copyright{position:absolute;left:0;top:354px;width:1200px;text-align:center;font-size:13px;color:var(--navy)}
</style>
</head>
<body>

<header class="site-header">
  <div class="brand">
    <div class="brand-mark"></div>
    <div class="brand-text">
      <div class="brand-owner">T. Marlow Quint</div>
      <div class="brand-name">Lanternfield Golf</div>
      <div class="brand-line">marlow.quint@lanternfield.golf</div>
      <div class="brand-phone">917-555-0148</div>
      <div class="brand-line">Jersey City , NJ<br>USA</div>
    </div>
  </div>
  <div class="top-btn phone">
    <svg width="12" height="12" viewBox="0 0 24 24" fill="#fff"><path d="M6.6 10.8a15 15 0 006.6 6.6l2.2-2.2a1 1 0 011-.25 11.4 11.4 0 003.6.57 1 1 0 011 1V20a1 1 0 01-1 1A17 17 0 013 4a1 1 0 011-1h3.5a1 1 0 011 1c0 1.25.2 2.45.57 3.57a1 1 0 01-.25 1z"/></svg>
    917 -555-0148
  </div>
  <div class="top-btn chat">
    <svg width="14" height="12" viewBox="0 0 28 24" fill="#fff"><path d="M2 2h15a2 2 0 012 2v8a2 2 0 01-2 2H8l-4 4v-4H2a2 2 0 01-2-2V4a2 2 0 012-2z"/><path d="M21 7h5a2 2 0 012 2v7a2 2 0 01-2 2h-1v4l-4-4h-6a2 2 0 01-2-2h4a4 4 0 004-4z"/></svg>
    Live Chat
  </div>
  <nav class="main-nav">
    <span class="active" style="left:519px">Home</span>
    <span style="left:597px">About Us</span>
    <span style="left:696px">Courses</span>
    <span style="left:791px">News</span>
    <span style="left:864px">Board of Directors</span>
    <span style="left:1029px">Contact</span>
  </nav>
</header>

<section class="hero" role="img" aria-label="Golfer finishing a swing on a sunlit fairway beside a pond">
  <h1 class="hero-title">LANTERNFIELD<br>GOLF</h1>
  <div class="btn">Contact Us</div>
</section>

<section class="about">
  <div class="about-photo" role="img" aria-label="Three golfers with their bags walking across a green fairway"></div>
  <h2 class="about-title">ABOUT<br>LANTERNFIELD GOLF</h2>
  <p class="about-copy">Lorem ipsum dolor sit amet, consectetur adipiscing elit, sed lordo eiusmod tempor incididunt ut labore et dolore magna lorealiqua. Quis ipsum suspendise ultrices gravida. Risus commodo vivlorerra maecenas accumsan lacus vel facilisis. Lorem ipsum dolor sit am et, consectetur adipiscing elit, sed dloo eiusmod tempor incididunt ut labore et dolore magna aliqua. Quis ipsum suspendisse ultrices gravida. Risus commodo viverra maecenas accumsan lacus vel facilisis. Lorem ipsum dolor sit amet, consectetur.</p>
  <div class="btn">Read More</div>
</section>

<section class="courses"></section>
<h2 class="section-title" style="top:1358px">OUR COURSES</h2>
<svg class="slider-arrow" style="left:76px" width="18" height="30" viewBox="0 0 18 30"><path d="M14 3L3 15l11 12" fill="none" stroke="#111" stroke-width="4"/></svg>
<svg class="slider-arrow" style="left:1106px" width="18" height="30" viewBox="0 0 18 30"><path d="M4 3l11 12L4 27" fill="none" stroke="#111" stroke-width="4"/></svg>

<article class="course-card" style="left:150px">
  <div class="course-photo" role="img" aria-label="Gloved hand placing a golf ball on a tee" style="background:linear-gradient(135deg,#c9d6a8 0%,#7fa04a 100%)"></div>
  <h3 class="course-name">Lorem ipsum dolor sit amet, consectetur</h3>
  <p class="course-desc">Lorem ipsum dolor sit amet, co nsectetur adipiscing elit, sed do eiusmod tempor incidid.</p>
  <div class="btn">Read More</div>
</article>
<article class="course-card" style="left:460px">
  <div class="course-photo" role="img" aria-label="Golfer swinging on a seaside course" style="background:linear-gradient(135deg,#a9c1cf 0%,#6e9a4a 100%)"></div>
  <h3 class="course-name">Lorem ipsum dolor sit amet, consectetur</h3>
  <p class="course-desc">Lorem ipsum dolor sit amet, co nsectetur adipiscing elit, sed do eiusmod tempor incidid.</p>
  <div class="btn">Read More</div>
</article>
<article class="course-card" style="left:771px">
  <div class="course-photo" role="img" aria-label="Golfers carrying bags toward the course" style="background:linear-gradient(135deg,#bcb1a8 0%,#4a4c50 100%)"></div>
  <h3 class="course-name">Lorem ipsum dolor sit amet, consectetur</h3>
  <p class="course-desc">Lorem ipsum dolor sit amet, co nsectetur adipiscing elit, sed do eiusmod tempor incidid.</p>
  <div class="btn">Read More</div>
</article>

<section class="discover">
  <div class="discover-photo" role="img" aria-label="Three smiling golfers holding clubs under a blue sky"></div>
  <div class="discover-accent"></div>
  <h2 class="discover-title">Discover Your<br>Best Game</h2>
  <p class="discover-copy">Lorem ipsum dolor sit amet, consectetur adipi scing elit, sed do eiusmod tempor incididunt ut labore et dolore magna aliqua. Quis ipsum suspendisse ultrices gravida.</p>
  <div class="btn">Read More</div>
</section>

<h2 class="section-title" style="top:2608px">MEET YOUR TEAM</h2>
<div class="member" style="left:151px">
  <div class="member-photo" role="img" aria-label="Team member in a white cap mid swing" style="background:linear-gradient(135deg,#dfe4d8 0%,#9cb077 100%)"></div>
  <div class="member-name">Reed Ashford</div><div class="member-role">Lorem Ipsum</div>
</div>
<div class="member" style="left:468px">
  <div class="member-photo" role="img" aria-label="Senior team member holding a club on the course" style="background:linear-gradient(135deg,#d2d2bf 0%,#8c9760 100%)"></div>
  <div class="member-name">Reed Ashford</div><div class="member-role">Lorem Ipsum</div>
</div>
<div class="member" style="left:785px">
  <div class="member-photo" role="img" aria-label="Team member in a blue shirt finishing a swing" style="background:linear-gradient(135deg,#b9cbd6 0%,#7a9e58 100%)"></div>
  <div class="member-name">Reed Ashford</div><div class="member-role">Lorem Ipsum</div>
</div>

<section class="events" role="img" aria-label="Golf course with trees and bunkers at dusk">
  <h2 class="section-title">CALEDAR EVENTS</h2>
  <div class="event-list">
    <div class="event" style="top:28px">
      <div class="event-date"><svg width="10" height="10" viewBox="0 0 10 10" fill="#fff"><rect x="0" y="2" width="10" height="8" rx="1"/><rect x="2" y="0" width="1.5" height="3"/><rect x="6.5" y="0" width="1.5" height="3"/></svg>Apr 06 2023</div>
      <div class="event-title">Lorem ipsum dolor sit ame cons lorem ipspectetur</div>
    </div>
    <div class="event" style="top:136px">
      <div class="event-date"><svg width="10" height="10" viewBox="0 0 10 10" fill="#fff"><rect x="0" y="2" width="10" height="8" rx="1"/><rect x="2" y="0" width="1.5" height="3"/><rect x="6.5" y="0" width="1.5" height="3"/></svg>Apr 06 2023</div>
      <div class="event-title">Lorem ipsum dolor sit ame consect lorem ispetur</div>
    </div>
    <div class="event" style="top:234px">
      <div class="event-date"><svg width="10" height="10" viewBox="0 0 10 10" fill="#fff"><rect x="0" y="2" width="10" height="8" rx="1"/><rect x="2" y="0" width="1.5" height="3"/><rect x="6.5" y="0" width="1.5" height="3"/></svg>Apr 06 2023</div>
      <div class="event-title">Lorem ilorempsum dolor sit amelo con sectetur</div>
    </div>
    <div class="event" style="top:338px">
      <div class="event-date"><svg width="10" height="10" viewBox="0 0 10 10" fill="#fff"><rect x="0" y="2" width="10" height="8" rx="1"/><rect x="2" y="0" width="1.5" height="3"/><rect x="6.5" y="0" width="1.5" height="3"/></svg>Apr 06 2023</div>
      <div class="event-title">Lorem ipsum dolor sit ame consect lorem ispetur</div>
    </div>
  </div>
  <div class="calendar">
    <div class="cal-month">April 2023</div>
    <svg class="cal-next" width="8" height="12" viewBox="0 0 8 12"><path d="M1 1l5 5-5 5" fill="none" stroke="#2b3152" stroke-width="1.5"/></svg>
    <div class="cal-add"><svg width="9" height="9" viewBox="0 0 10 10"><circle cx="5" cy="5" r="4.3" fill="none" stroke="#4aa85a"/><path d="M5 3v4M3 5h4" stroke="#4aa85a"/></svg>Add Event</div>
    <div class="cal-grid">
      <span class="head" style="left:52px;top:0">SUN</span><span class="head" style="left:134px;top:0">MON</span><span class="head" style="left:217px;top:0">TUE</span><span class="head" style="left:299px;top:0">WED</span><span class="head" style="left:380px;top:0">THU</span><span class="head" style="left:461px;top:0">FRI</span><span class="head" style="left:543px;top:0">SAT</span>

      <span class="off" style="left:52px;top:53px">28</span><span class="off" style="left:134px;top:53px">29</span><span class="off" style="left:217px;top:53px">30</span><span class="off" style="left:299px;top:53px">31</span><span class="dim" style="left:380px;top:53px">1</span><span class="dim" style="left:461px;top:53px">2</span><span class="dim" style="left:543px;top:53px">3</span>

      <span class="dim" style="left:52px;top:110px">4</span><span class="dim" style="left:134px;top:110px">5</span><span class="dim" style="left:217px;top:110px">6</span><span class="dim" style="left:299px;top:110px">7</span><span class="dim" style="left:380px;top:110px">8</span><span class="dim" style="left:461px;top:110px">9</span><span class="dim" style="left:543px;top:110px">10</span>

      <span class="dim" style="left:52px;top:166px">11</span><span class="dim" style="left:134px;top:166px">12</span><span class="dim" style="left:217px;top:166px">13</span><span style="left:299px;top:166px">14</span><span style="left:380px;top:166px">15</span><span style="left:461px;top:166px">16</span><span style="left:543px;top:166px">17</span>

      <span style="left:52px;top:222px">18</span><span style="left:134px;top:222px">19</span><span style="left:217px;top:222px">20</span><span style="left:299px;top:222px">21</span><span style="left:380px;top:222px">22</span><span style="left:461px;top:222px">23</span><span style="left:543px;top:222px">24</span>

      <span style="left:52px;top:278px">25</span><span style="left:134px;top:278px">26</span><span style="left:217px;top:278px">27</span><span style="left:299px;top:278px">28</span><span style="left:380px;top:278px">29</span><span style="left:461px;top:278px">30</span><span class="off" style="left:543px;top:278px">1</span>

      <i class="dot" style="left:50px;top:188px;background:#3f73c8"></i>
      <i class="dot" style="left:215px;top:188px;background:#e07a2c"></i>
      <i class="dot" style="left:375px;top:188px;background:#3f73c8"></i>
      <i class="dot" style="left:381px;top:188px;background:#e07a2c"></i>
      <i class="dot" style="left:132px;top:244px;background:#4aa85a"></i>
      <i class="dot" style="left:541px;top:244px;background:#4aa85a"></i>
    </div>
  </div>
</section>

<footer class="site-footer">
  <div class="footer-brand">
    <div class="brand-mark"></div>
    <div class="brand-text">
      <div class="brand-owner">T. Marlow Quint</div>
      <div class="brand-name">Lanternfield Golf</div>
      <div class="brand-line">marlow.quint@lanternfield.golf</div>
      <div class="brand-phone">917-555-0148</div>
      <div class="brand-line">Jersey City , NJ<br>USA</div>
    </div>
  </div>
  <div class="divider" style="left:397px"></div>
  <div class="divider" style="left:517px"></div>
  <div class="divider" style="left:784px"></div>

  <div class="footer-col-title" style="left:424px">Links</div>
  <div class="footer-links">Home<br>About Us<br>Courses<br>Events<br>News<br>Contact Us</div>

  <div class="footer-col-title" style="left:569px">Contact</div>
  <div class="contact-item" style="top:104px">
    <div class="contact-icon"><svg width="14" height="16" viewBox="0 0 14 18" fill="#fff"><path d="M7 0a7 7 0 017 7c0 5-7 11-7 11S0 12 0 7a7 7 0 017-7zm0 4a3 3 0 100 6 3 3 0 000-6z"/></svg></div>
    <div>418 Calloway St<br>Suite 307C<br>Jersey City, NJ, 07348</div>
  </div>
  <div class="contact-item" style="top:178px">
    <div class="contact-icon"><svg width="14" height="14" viewBox="0 0 24 24" fill="#fff"><path d="M6.6 10.8a15 15 0 006.6 6.6l2.2-2.2a1 1 0 011-.25 11.4 11.4 0 003.6.57 1 1 0 011 1V20a1 1 0 01-1 1A17 17 0 013 4a1 1 0 011-1h3.5a1 1 0 011 1c0 1.25.2 2.45.57 3.57a1 1 0 01-.25 1z"/></svg></div>
    <div>Phone:<br>917-555-0148</div>
  </div>
  <div class="contact-item" style="top:236px">
    <div class="contact-icon"><svg width="15" height="11" viewBox="0 0 16 12"><rect x="0.5" y="0.5" width="15" height="11" rx="1" fill="#fff"/><path d="M1 1l7 6 7-6" fill="none" stroke="#e4a812" stroke-width="1.4"/></svg></div>
    <div>Email:<br>info@lanternfieldmail.com</div>
  </div>

  <div class="footer-col-title" style="left:825px">Newsletter Sign up</div>
  <p class="news-copy">Lorem ipsum dolor sit amet locon sectetur adipiscing elit.</p>
  <div class="news-input">Email:</div>
  <div class="news-btn">SIGN UP</div>

  <div class="footer-rule"></div>
  <div class="copyright">Copyright © 2023 Lanternfield Golf. All rights reserved.</div>
</footer>

</body>
</html>
```